Rug Cleaning Web Design Project

We need a web design for our cleaning company. We currently have a web page but are not happy with its design. We currently offer fine rug cleaning,upholstery cleaning, and residential and commercial carpet cleanning. We also offer water damage restoration. For our rug cleaning services we offer : Enzyme treatments for pet contamination and odor removal, application of stain protection that is designed for the fine textiles used in rug construction, application of treatments designed to prevent moth damage and pads designed to be used under rugs.Our current web site is harborfreshcare.example. We are intrested in a design with similar information to the web page of Velmora Rug Cleaners INC. We would like to use the colors that are present in our logo that will be uploaded with this description. We would also like this new page to be linked to our other address loomrinsepro.example. We would like the deign to be visually attractive but not "too busy".
Updates

Please include pictures of rugs, or people washing rugs if possible. We do not offer maid type cleaning services. We would not be interested in designs including pictures depicting that type service. Thanks for your hard work on this project.

Dana Whitlow

Industry/Entity Type

Residential

Requirements
Must have
• This page must be viewable on smart phones and tablets.

```html
<!DOCTYPE html>
<html lang="en">
<head>
<meta charset="utf-8">
<meta name="viewport" content="width=1200">
<title>LoomRinse Pro – Harbor Fresh Care</title>
<link rel="stylesheet" href="https://fonts.googleapis.com/css2?family=Source+Sans+3:wght@300;400;600&display=swap">
<style>
:root{
  --brand-blue:#0a62b8;
  --brand-blue-light:#2f9bf0;
  --link-blue:#0b6fc7;
  --text:#444;
  --text-dark:#222;
  --rule:#dcdcdc;
  --panel:#f1f1f1;
  --footer:#f0f0f0;
  --button:#1e1e1e;
}
*{box-sizing:border-box;margin:0;padding:0}
html,body{width:1200px;height:1119px;overflow:hidden;background:#fff}
body{font-family:"Source Sans 3",Arial,sans-serif;color:var(--text);position:relative;font-size:12px}
.abs{position:absolute}
.top-rule{left:0;top:0;width:1200px;border-top:1px dotted #9ab}
/* header */
.brand{left:171px;top:20px;display:flex;align-items:center;gap:10px}
.brand-mark{width:40px;height:40px;border-radius:50%;background:var(--brand-blue)}
.brand-name{font-size:30px;font-weight:600;color:var(--text-dark);line-height:1}
.brand-sub{font-size:11px;letter-spacing:2px;color:var(--text-dark);font-weight:600}
.contact-head{left:620px;top:30px;text-align:right;width:173px}
.contact-head .phone{font-size:21px;color:var(--link-blue);font-weight:300;display:flex;align-items:center;justify-content:flex-end;gap:8px}
.contact-head .email{font-size:12px;color:var(--text-dark);margin-top:4px}
.head-divider{left:815px;top:20px;height:65px;border-left:1px solid var(--rule)}
.search{left:843px;top:38px;display:flex}
.search input{width:131px;height:26px;border:1px solid #ccc}
.search button{width:61px;height:26px;margin-left:3px;border:0;background:linear-gradient(#48a8ef,#1579cc);color:#fff;font-family:inherit;font-size:12px;letter-spacing:.5px}
/* band */
.band{left:0;top:103px;width:1200px;height:392px;background:radial-gradient(ellipse 160px 300px at 1060px 200px,var(--brand-blue-light),transparent 80%),radial-gradient(ellipse 80px 200px at 150px 320px,#3aa0f2,transparent 80%),var(--brand-blue)}
.nav{left:171px;top:108px;width:868px;height:37px;display:flex;background:linear-gradient(#fff,#e9e9e9);border-bottom:2px solid var(--brand-blue)}
.nav a{flex:auto;display:flex;align-items:center;justify-content:center;color:var(--brand-blue);text-decoration:none;font-size:12px;font-weight:600;letter-spacing:.6px;border-right:1px solid #d6d6d6}
.nav a:last-child{border-right:0}
.slider{left:171px;top:146px;width:868px;height:410px;background:linear-gradient(100deg,#e6e6e2 0%,#cfcbc4 45%,#8f877d 70%,#d9d8d3 100%);box-shadow:0 10px 12px -8px rgba(0,0,0,.45)}
.dots{left:203px;top:504px;display:flex;gap:5px}
.dots span{width:16px;height:16px;border-radius:50%;background:#111}
.dots span.on{background:var(--brand-blue);border:3px solid #111}
/* sections */
.panel-title{height:36px;background:linear-gradient(#fafafa,#ececec);border:1px solid #e2e2e2;color:var(--brand-blue);font-size:17px;font-weight:300;padding-left:12px;display:flex;align-items:center;text-transform:uppercase}
.welcome-title{left:168px;top:585px;width:561px}
.welcome-photo{left:170px;top:642px;width:151px;height:105px;background:linear-gradient(90deg,#c9dbe6,#e7c0c3 60%,#c2252c)}
.welcome-lead{left:340px;top:641px;width:385px;color:var(--link-blue);font-size:12px;line-height:16px;font-weight:600}
.welcome-body{left:340px;top:699px;width:385px;font-size:12px;line-height:18.5px}
.contact-title{left:167px;top:790px;width:250px}
.contact-info{left:180px;top:838px}
.contact-info .org{font-size:17px;color:var(--text);font-weight:400}
.contact-info .addr{color:var(--link-blue);line-height:22px;margin-top:3px}
.contact-info .note{margin-top:6px}
.news-title{left:449px;top:790px;width:279px}
.newsletter{left:449px;top:837px;width:281px}
.newsletter label{display:block;font-size:12px;color:var(--text-dark);margin-bottom:5px}
.newsletter input{display:block;width:281px;height:26px;border:1px solid #ccc;margin-bottom:15px;margin-left:1px}
.btn{background:var(--button);color:#fff;font-family:inherit;font-size:13px;border:0;height:33px;padding:0 11px}
.signup{left:451px;top:942px}
.services-title{left:757px;top:586px;width:280px;background:linear-gradient(#1a7fd6,#0a5fb5);color:#fff;border:0;padding-left:9px;font-size:18px}
.service{left:759px;width:274px;display:flex;gap:10px;border-bottom:1px solid #e3e3e3;padding-bottom:12px}
.service .thumb{width:91px;height:80px;flex:none}
.service h3{font-size:15px;font-weight:300;color:var(--link-blue);line-height:18px;text-transform:uppercase;margin-top:-4px}
.service p{font-size:12px;line-height:18.5px;margin:4px 0 0 2px;color:var(--text-dark)}
.svc1{top:638px}.svc2{top:742px}.svc3{top:849px;border-bottom:0}
.t1{background:linear-gradient(#bcd6ee,#d8cdb8 60%,#5f8a3c)}
.t2{background:linear-gradient(120deg,#9ec3cc,#e6eef0 50%,#5d6f74)}
.t3{background:linear-gradient(#e7e2da 60%,#c2172a)}
.readmore{left:759px;top:942px}
/* footer */
.footer{left:0;top:1003px;width:1200px;height:116px;background:var(--footer);border-top:1px dotted #999}
.footer-nav{left:182px;top:1042px;font-size:11px;color:var(--text-dark)}
.footer-nav a{color:inherit;text-decoration:none}
.footer-nav .sep{margin:0 7px}
.copyright{left:182px;top:1066px;font-size:11px;color:var(--text-dark)}
.follow{left:959px;top:1042px;font-size:11px;color:var(--text-dark)}
.social{left:935px;top:1067px;display:flex;gap:4px}
.social span{width:18px;height:18px;background:var(--link-blue);border-radius:2px}
.social span:last-child{background:#e8751a}
</style>
</head>
<body>
<div class="abs top-rule"></div>

<header>
  <div class="abs brand">
    <span class="brand-mark"></span>
    <div>
      <div class="brand-name">LoomRinse Pro</div>
      <div class="brand-sub">HARBOR FRESH CARE, LLC</div>
    </div>
  </div>
  <div class="abs contact-head">
    <div class="phone">
      <svg width="20" height="18" viewBox="0 0 20 18" aria-hidden="true"><path d="M2 6c0-3 4-4 8-4s8 1 8 4l-3 1-1-2H6L5 7z M5 9h10l2 7H3z" fill="#111"/><circle cx="10" cy="12" r="2" fill="#fff"/></svg>
      (555) 014-2710
    </div>
    <div class="email">hello@harborfreshcare.example</div>
  </div>
  <div class="abs head-divider"></div>
  <form class="abs search"><input type="text" aria-label="Search"><button type="button">SEARCH</button></form>
</header>

<div class="abs band"></div>
<nav class="abs nav">
  <a href="#">HOME</a><a href="#">ABOUT US</a><a href="#">RUG WASHING</a><a href="#">WATER DAMAGE</a><a href="#">CARPET CLEANING</a><a href="#">CONTACT US</a>
</nav>
<div class="abs slider" role="img" aria-label="Slideshow photo of a bright kitchen being cleaned"></div>
<div class="abs dots"><span></span><span class="on"></span><span></span><span></span><span></span></div>

<main>
  <h2 class="abs panel-title welcome-title">Welcome to our site</h2>
  <div class="abs welcome-photo" role="img" aria-label="Photo of a person wiping a window"></div>
  <p class="abs welcome-lead">When it comes to cleaning carpet, oriental rugs, area rugs or furniture ~ any fabric from antique silk brocades to contemporary carpet fibers ~ our service is unparalled.</p>
  <p class="abs welcome-body">Harbor Fresh Care &amp; Restoration is the recipient of the 2010 &amp; 2011"Best in Business Award" in Brookvale, Alabama for Water Damage Restoration and Carpet and Rug Cleaning.</p>

  <h2 class="abs panel-title contact-title">Contact us</h2>
  <div class="abs contact-info">
    <div class="org">Harbor Fresh Care &amp; Restoration</div>
    <div class="addr">48 Alder Creek Road Brookvale,<br>AL&nbsp; 35000</div>
    <div class="note">Serving Brookvale and surrounding areas.</div>
  </div>

  <h2 class="abs panel-title news-title">Newsletter signup</h2>
  <form class="abs newsletter">
    <label for="nl-name">Enter the Name</label><input id="nl-name" type="text">
    <label for="nl-email">Enter the E mail id</label><input id="nl-email" type="email">
  </form>
  <button class="abs btn signup" type="button">SIGN UP</button>

  <h2 class="abs panel-title services-title">Our services</h2>
  <article class="abs service svc1">
    <div class="thumb t1" role="img" aria-label="Photo of a family house"></div>
    <div><h3>Residential<br>Cleaning</h3><p>Your home will look and smell just like it should!</p></div>
  </article>
  <article class="abs service svc2">
    <div class="thumb t2" role="img" aria-label="Photo of an escalator in a commercial building"></div>
    <div><h3>Commercial<br>Cleaning</h3><p>We adhere to OSHA standards and go above and beyond!</p></div>
  </article>
  <article class="abs service svc3">
    <div class="thumb t3" role="img" aria-label="Photo of a rug being vacuumed"></div>
    <div><h3>Rug<br>Cleaning</h3><p>We adhere to OSHA standards and go above and beyond!</p></div>
  </article>
  <button class="abs btn readmore" type="button">READ MORE</button>
</main>

<footer>
  <div class="abs footer"></div>
  <div class="abs footer-nav">
    <a href="#">Home</a><span class="sep">|</span><a href="#">About Us</a><span class="sep">|</span><a href="#">Rug Washing</a><span class="sep">|</span><a href="#">Water Damage</a><span class="sep">|</span><a href="#">Carpet Cleaning</a><span class="sep">|</span><a href="#">Contact Us</a>
  </div>
  <div class="abs copyright">Copyrights @ 2012 All Rights Reserved</div>
  <div class="abs follow">Follow Us on</div>
  <div class="abs social" aria-label="Social links"><span></span><span></span><span></span><span></span></div>
</footer>
</body>
</html>
```